Business Card Design

Selling Televisions, Velmora, Kira, Dravelux, Ronavi
The latest models, sizes ranging from 22"- 75"
Surround Sounds, Sound Bars and Wall Mounts

Target Market(s)

Mainly males/boys/blokes etc

Industry/Entity Type

Business

Contact Information for Business Card

Glen Marsh
07841526094
glmarsh@quinvale-mail.com

Requirements
Must have
• simplistic design, probably just 2 of the images used

clarity essential
Nice to have
• Metallic if possible

```html
<!DOCTYPE html>
<html lang="en">
<head>
<meta charset="utf-8">
<title>Glen Marsh – Business Card</title>
<link href="https://fonts.googleapis.com/css2?family=Lato:wght@700;900&display=swap" rel="stylesheet">
<style>
  :root {
    --backdrop: #6a6a6a;
    --ink: #111111;
    --rule: #2a2a2a;
    --metal-light: #e4e4e4;
    --metal-mid: #b5b5b5;
    --metal-dark: #8e8e8e;
    --band-dark: #1c1d20;
    --band-mid: #3a3c41;
    --chrome-hi: #f7f7f7;
    --chrome-lo: #7d7d7d;
    --frame-white: #ffffff;
    --frame-line: #4a4a4a;
  }
  html, body {
    margin: 0;
    width: 1200px;
    height: 900px;
    overflow: hidden;
    background: var(--backdrop);
  }
  .card {
    position: absolute;
    left: 100px;
    top: 160px;
    width: 1000px;
    height: 580px;
    border-radius: 28px;
    overflow: hidden;
  }
  .card-art {
    position: absolute;
    inset: 0;
    width: 100%;
    height: 100%;
  }
  .card-details {
    position: absolute;
    left: 490px;
    top: 178px;
    width: 480px;
    font-family: "Lato", sans-serif;
    color: var(--ink);
  }
  .owner-name {
    margin: 0;
    font-weight: 900;
    font-size: 48px;
    letter-spacing: 0.5px;
    line-height: 1;
  }
  .name-rule {
    height: 3px;
    background: var(--rule);
    margin: 24px -30px 30px -10px;
  }
  .contact-line {
    margin: 0 0 8px;
    font-weight: 700;
    font-size: 30px;
    line-height: 1.2;
  }
</style>
</head>
<body>
  <div class="card">
    <svg class="card-art" viewBox="0 0 1000 580" xmlns="http://www.w3.org/2000/svg">
      <defs>
        <linearGradient id="brushed-metal" x1="0" y1="0" x2="1" y2="1">
          <stop offset="0" stop-color="var(--metal-mid)"/>
          <stop offset="0.35" stop-color="var(--metal-light)"/>
          <stop offset="0.6" stop-color="var(--metal-mid)"/>
          <stop offset="0.85" stop-color="var(--metal-light)"/>
          <stop offset="1" stop-color="var(--metal-dark)"/>
        </linearGradient>
        <linearGradient id="chrome-edge" x1="0" y1="0" x2="0" y2="1">
          <stop offset="0" stop-color="var(--chrome-hi)"/>
          <stop offset="0.5" stop-color="var(--chrome-lo)"/>
          <stop offset="1" stop-color="var(--chrome-hi)"/>
        </linearGradient>
        <linearGradient id="band-fill" x1="0" y1="0" x2="0" y2="1">
          <stop offset="0" stop-color="var(--band-mid)"/>
          <stop offset="0.5" stop-color="var(--band-dark)"/>
          <stop offset="1" stop-color="var(--band-mid)"/>
        </linearGradient>
        <linearGradient id="photo-lake" x1="0" y1="0" x2="0" y2="1">
          <stop offset="0" stop-color="#6f86b5"/>
          <stop offset="0.55" stop-color="#c59aa6"/>
          <stop offset="1" stop-color="#2c3c5a"/>
        </linearGradient>
        <linearGradient id="photo-showroom" x1="0" y1="0" x2="0" y2="1">
          <stop offset="0" stop-color="#b9c4cc"/>
          <stop offset="0.45" stop-color="#7b6aa8"/>
          <stop offset="0.7" stop-color="#d9894f"/>
          <stop offset="1" stop-color="#d7d7d7"/>
        </linearGradient>
        <linearGradient id="photo-city" x1="0" y1="0" x2="0" y2="1">
          <stop offset="0" stop-color="#3e5d9c"/>
          <stop offset="0.5" stop-color="#4a3b6e"/>
          <stop offset="1" stop-color="#c99a55"/>
        </linearGradient>
      </defs>

      <!-- metal base -->
      <rect class="metal-base" width="1000" height="580" fill="url(#brushed-metal)"/>

      <!-- white tile field on the left -->
      <polygon class="tile-field" points="0,0 230,0 420,290 230,580 0,580" fill="var(--frame-white)"/>

      <!-- top band -->
      <g class="top-band">
        <rect x="140" y="14" width="860" height="12" fill="url(#chrome-edge)"/>
        <rect x="140" y="26" width="860" height="62" fill="url(#band-fill)" role="img" aria-label="Perforated dark metal strip"/>
        <rect x="140" y="88" width="860" height="12" fill="url(#chrome-edge)"/>
      </g>

      <!-- bottom band -->
      <g class="bottom-band">
        <rect x="360" y="482" width="640" height="12" fill="url(#chrome-edge)"/>
        <rect x="360" y="494" width="640" height="62" fill="url(#band-fill)" role="img" aria-label="Perforated dark metal strip"/>
        <rect x="360" y="556" width="640" height="12" fill="url(#chrome-edge)"/>
      </g>

      <!-- product tiles -->
      <g class="product-tile tile-top">
        <polygon points="60,-110 250,80 60,270 -130,80" fill="var(--frame-white)" stroke="var(--frame-line)" stroke-width="2"/>
        <polygon points="60,-88 228,80 60,248 -108,80" fill="url(#photo-lake)" role="img" aria-label="Flat-screen television showing a lake at dusk"/>
      </g>
      <g class="product-tile tile-centre">
        <polygon points="300,110 480,290 300,470 120,290" fill="var(--frame-white)" stroke="var(--frame-line)" stroke-width="2"/>
        <polygon points="300,132 458,290 300,448 142,290" fill="url(#photo-showroom)" role="img" aria-label="Curved television on display in a bright showroom"/>
      </g>
      <g class="product-tile tile-bottom">
        <polygon points="60,310 250,500 60,690 -130,500" fill="var(--frame-white)" stroke="var(--frame-line)" stroke-width="2"/>
        <polygon points="60,332 228,500 60,668 -108,500" fill="url(#photo-city)" role="img" aria-label="Television showing a city skyline at night"/>
      </g>
    </svg>

    <div class="card-details">
      <h1 class="owner-name">GLEN MARSH</h1>
      <div class="name-rule"></div>
      <p class="contact-line">07841526094</p>
      <p class="contact-line">glmarsh@quinvale-mail.com</p>
    </div>
  </div>
</body>
</html>
```